Упаковка для Ровен
Задание на дизайн
Приоритеты объектов в упаковке
Иллюстрация
Размеры
Опишите свою организацию или продукт и целевую аудиторию
размер упаковки размер 77х152х151, описание: Торт напоминающий легендарные батончики,
но менее сладкий, более мягкий, сочный и кремовый.
Ореховая нуга на темном песочном корже, политая
сливочной карамелью, сверху бисквит «брауни» с тонким
слоем какао крема, торт покрыт какао-глазурью с орехами.
Шесть слоев, ни один из которых не повторяется.
Уникальный каскад вкусов и текстур.
Тянется, хрустит и заставляет жмуриться от удовольствия!
Приложите логотипы или другие материалы
Дизайн ориентир
Текущая упаковка
Комментарии и пожелания для дизайнеров
Торт "Тойви пай" , нужен дизайн в американском стиле. Прошу обратить внимание название торта "Тойви пай".

```html
<!DOCTYPE html>
<html lang="ru">
<head>
<meta charset="utf-8">
<title>Тойви пай — упаковка Ровен</title>
<link href="https://fonts.googleapis.com/css2?family=Rubik:wght@500;800&display=swap" rel="stylesheet">
<style>
  :root {
    --bg: #e9e2d4;
    --cream: #ece6d7;
    --mauve: #a55d6c;
    --wine: #7a1f2a;
    --brown: #6e2a1a;
    --cake-dark: #4a2516;
    --cake-mid: #8a5030;
    --cake-light: #e8d8b8;
  }
  * { box-sizing: border-box; margin: 0; padding: 0; }
  html, body {
    width: 1200px; height: 1200px; overflow: hidden;
    background: var(--bg);
    font-family: "Rubik", sans-serif;
  }
  .canvas { position: relative; width: 1200px; height: 1200px; }

  .lid {
    position: absolute; left: 250px; top: 60px;
    width: 700px; height: 700px;
    background: var(--cream);
    overflow: hidden;
  }
  .lid-ornament {
    position: absolute; inset: 0;
    border: 70px solid var(--mauve);
  }
  .title-plate {
    position: absolute; left: 150px; top: 110px;
    width: 330px; height: 190px;
    background: var(--mauve);
    padding: 22px 28px;
    color: var(--cream);
  }
  .brand {
    display: flex; align-items: center; gap: 8px;
    font-size: 15px; font-weight: 500; line-height: 1; margin-bottom: 14px;
  }
  .brand-dot { width: 10px; height: 10px; border-radius: 50%; background: var(--cream); flex: none; }
  .product-name {
    font-size: 56px; font-weight: 800; line-height: 1.08;
    text-transform: uppercase; letter-spacing: 0;
  }
  .tagline {
    position: absolute; left: 150px; top: 322px;
    font-size: 18px; font-weight: 800; color: var(--brown);
  }
  .cake-photo {
    position: absolute; left: 150px; top: 360px;
    width: 430px; height: 220px;
    background: linear-gradient(180deg, var(--cake-dark) 0%, var(--cake-mid) 40%, var(--cake-light) 62%, var(--cake-dark) 100%);
    border-radius: 6px;
  }

  .side {
    position: absolute; left: 250px; top: 780px;
    width: 700px; height: 355px;
    background: var(--cream);
    display: flex; align-items: center; justify-content: space-around;
    padding: 0 20px;
  }
  .side-label {
    width: 150px; padding: 16px 16px;
    color: var(--cream);
  }
  .side-label.wine { background: var(--wine); }
  .side-label.mauve { background: var(--mauve); }
  .side-label .brand { font-size: 11px; margin-bottom: 8px; gap: 6px; }
  .side-label .brand-dot { width: 7px; height: 7px; }
  .side-label .product-name { font-size: 27px; }
  .side-photo {
    width: 150px; height: 130px; border-radius: 4px;
    background: linear-gradient(180deg, var(--cake-dark) 0%, var(--cake-mid) 40%, var(--cake-light) 62%, var(--cake-dark) 100%);
  }
</style>
</head>
<body>
<main class="canvas">
  <section class="lid">
    <div class="lid-ornament" role="img" aria-label="Декоративный орнамент по краю крышки"></div>
    <div class="title-plate">
      <div class="brand"><span class="brand-dot"></span>Ровен</div>
      <h1 class="product-name">Тойви<br>пай</h1>
    </div>
    <p class="tagline">мягкий, сочный и кремовый</p>
    <div class="cake-photo" role="img" aria-label="Фото куска торта с ореховой глазурью, нугой и карамелью"></div>
  </section>

  <section class="side">
    <div class="side-label wine">
      <div class="brand"><span class="brand-dot"></span>Ровен</div>
      <div class="product-name">Тойви<br>пай</div>
    </div>
    <div class="side-photo" role="img" aria-label="Фото куска торта"></div>
    <div class="side-label mauve">
      <div class="brand"><span class="brand-dot"></span>Ровен</div>
      <div class="product-name">Тойви<br>пай</div>
    </div>
    <div class="side-photo" role="img" aria-label="Фото куска торта сбоку"></div>
  </section>
</main>
</body>
</html>
```